Real Estate - Large Sign Design

I am looking for a fresh new look for our leasing signs that will be showcase in front of commercial buildings available for lease. The sign dimension can be either 8'x4' or 4'x8'. They must exemplify our brand (see attachments) and be very visible by people driving by at high speeds.
They must include the following:
- Our logo (vector attached)
- Office Space Available
- 555-018-3274
- Nell Ruby
- Carl Ivey
- www.vantorile.com
Please let me know if you have any questions.
Target Market(s)
Drivers in high traffic areas, walking crowds
Industry/Entity Type
Real Estate
Requirements
Must have
- They must include the following:
- - Our logo (vector attached)
- - Office Space Available
- - 555-018-3274
- - Nell Ruby
- - Carl Ivey
- - www.vantorile.com
Should not have
- Should not be busy or hard to read.

```html
<!DOCTYPE html>
<html lang="en">
<head>
<meta charset="utf-8">
<title>Office Space Available – Leasing Signs</title>
<link rel="stylesheet" href="https://fonts.googleapis.com/css2?family=Oswald:wght@400;500&family=Jost:wght@400;500;600&display=swap">
<style>
  :root {
    --bg: #2b2b2b;
    --white: #ffffff;
    --green: #0b9444;
    --green-deep: #1e7a45;
    --lime: #8dc63f;
    --slate: #3f4b4a;
    --slate-blue: #444a5c;
  }
  html, body { margin: 0; padding: 0; overflow: hidden; }
  body { width: 1200px; height: 901px; background: var(--bg); position: relative; }
  .sign { position: absolute; background: var(--white); overflow: hidden; }
  .sign svg.shapes { position: absolute; inset: 0; width: 100%; height: 100%; }
  .sign--wide-a { left: 87px; top: 102px; width: 663px; height: 330px; }
  .sign--wide-b { left: 87px; top: 468px; width: 663px; height: 328px; }
  .sign--tall   { left: 785px; top: 119px; width: 330px; height: 661px; }

  .txt { position: absolute; line-height: 1; white-space: nowrap; }
  .headline { font-family: "Oswald", sans-serif; font-weight: 400; color: var(--green); text-transform: uppercase; }
  .names { font-family: "Jost", sans-serif; font-weight: 500; color: var(--slate); text-transform: uppercase; }
  .phone { font-family: "Jost", sans-serif; font-weight: 500; color: var(--slate); }
  .web { font-family: "Jost", sans-serif; font-weight: 600; color: var(--slate); }
  .brand { font-family: "Jost", sans-serif; font-weight: 500; color: var(--white); text-transform: uppercase; line-height: 1.05; text-align: left; }

  /* Sign A */
  .sign--wide-a .web { left: 0; width: 330px; text-align: center; top: 16px; font-size: 16px; }
  .sign--wide-a .headline { left: 38px; font-size: 84px; letter-spacing: -1px; }
  .sign--wide-a .headline.l1 { top: 38px; }
  .sign--wide-a .headline.l2 { top: 128px; }
  .sign--wide-a .names { left: 122px; top: 240px; font-size: 19px; }
  .sign--wide-a .phone { left: 44px; top: 260px; font-size: 52px; }
  .sign--wide-a .brand { left: 520px; top: 18px; font-size: 21px; }

  /* Sign B */
  .sign--wide-b .headline { left: 0; width: 490px; text-align: center; font-size: 64px; }
  .sign--wide-b .headline.l1 { top: 100px; }
  .sign--wide-b .headline.l2 { top: 170px; }
  .sign--wide-b .names { left: 0; width: 490px; text-align: center; top: 244px; font-size: 19px; }
  .sign--wide-b .phone { left: 0; width: 490px; text-align: center; top: 262px; font-size: 52px; }
  .sign--wide-b .brand { left: 520px; top: 20px; font-size: 21px; }
  .sign--wide-b .web { left: 524px; top: 147px; font-size: 14px; color: var(--white); }

  /* Tall sign */
  .sign--tall .headline { left: 28px; font-size: 66px; color: var(--slate); transform: scaleX(0.82); transform-origin: left top; }
  .sign--tall .headline.l1 { top: 162px; }
  .sign--tall .headline.l2 { top: 238px; }
  .sign--tall .headline.l3 { top: 314px; }
  .sign--tall .names { left: 30px; font-family: "Oswald", sans-serif; font-weight: 400; font-size: 30px; transform: scaleX(0.9); transform-origin: left top; }
  .sign--tall .names.n1 { top: 418px; }
  .sign--tall .names.n2 { top: 458px; }
  .sign--tall .phone { left: 28px; top: 500px; font-family: "Oswald", sans-serif; font-weight: 400; font-size: 52px; transform: scaleX(0.9); transform-origin: left top; }
  .sign--tall .brand { left: 190px; top: 34px; font-size: 19px; }
  .sign--tall .web { left: 28px; top: 614px; font-size: 22px; color: var(--white); }
</style>
</head>
<body>

<section class="sign sign--wide-a" aria-label="Horizontal leasing sign">
  <svg class="shapes" viewBox="0 0 663 330" preserveAspectRatio="none" aria-hidden="true">
    <defs>
      <linearGradient id="a-panel" x1="0" y1="0" x2="0" y2="1">
        <stop offset="0" stop-color="#1f8a4c"/>
        <stop offset="1" stop-color="#3e5a54"/>
      </linearGradient>
    </defs>
    <polygon points="443,0 663,0 663,330 589,330" fill="url(#a-panel)"/>
    <polygon points="443,0 663,0 663,134 492,112" fill="var(--green)"/>
  </svg>
  <span class="txt web">www.vantorile.com</span>
  <span class="txt headline l1">Office Space</span>
  <span class="txt headline l2">Available</span>
  <span class="txt names">Nell Ruby &amp; Carl Ivey</span>
  <span class="txt phone">555-018-3274</span>
  <span class="txt brand">Ashgrove<br>Realty<br>Group</span>
</section>

<section class="sign sign--wide-b" aria-label="Horizontal leasing sign, alternate">
  <svg class="shapes" viewBox="0 0 663 328" preserveAspectRatio="none" aria-hidden="true">
    <defs>
      <linearGradient id="b-band" x1="0" y1="0" x2="1" y2="0">
        <stop offset="0" stop-color="var(--lime)"/>
        <stop offset="1" stop-color="var(--green)"/>
      </linearGradient>
      <linearGradient id="b-panel" x1="0" y1="0" x2="0" y2="1">
        <stop offset="0" stop-color="#1f8a4c"/>
        <stop offset="1" stop-color="#3e5a54"/>
      </linearGradient>
    </defs>
    <polygon points="0,0 663,0 663,130 0,28" fill="url(#b-band)"/>
    <polygon points="478,0 663,0 663,328 500,328" fill="url(#b-panel)"/>
    <polygon points="478,0 663,0 663,130 488,104" fill="var(--green)"/>
  </svg>
  <span class="txt headline l1">Office Space</span>
  <span class="txt headline l2">Available</span>
  <span class="txt names">Nell Ruby &amp; Carl Ivey</span>
  <span class="txt phone">555-018-3274</span>
  <span class="txt brand">Ashgrove<br>Realty<br>Group</span>
  <span class="txt web">www.vantorile.com</span>
</section>

<section class="sign sign--tall" aria-label="Vertical leasing sign">
  <svg class="shapes" viewBox="0 0 330 661" preserveAspectRatio="none" aria-hidden="true">
    <defs>
      <linearGradient id="t-top" x1="0" y1="0" x2="1" y2="0">
        <stop offset="0" stop-color="var(--lime)"/>
        <stop offset="1" stop-color="var(--green)"/>
      </linearGradient>
      <linearGradient id="t-panel" x1="0" y1="0" x2="0" y2="1">
        <stop offset="0" stop-color="#1f8a4c"/>
        <stop offset="1" stop-color="var(--slate-blue)"/>
      </linearGradient>
      <linearGradient id="t-foot" x1="0" y1="0" x2="1" y2="0">
        <stop offset="0" stop-color="var(--green-deep)"/>
        <stop offset="1" stop-color="var(--lime)"/>
      </linearGradient>
    </defs>
    <polygon points="134,0 330,0 330,440" fill="url(#t-panel)"/>
    <polygon points="134,0 330,0 330,118 185,106" fill="url(#t-top)"/>
    <polygon points="0,564 330,614 330,661 0,661" fill="url(#t-foot)"/>
  </svg>
  <span class="txt headline l1">Office</span>
  <span class="txt headline l2">Space</span>
  <span class="txt headline l3">Available</span>
  <span class="txt names n1">Nell Ruby</span>
  <span class="txt names n2">Carl Ivey</span>
  <span class="txt phone">555-018-3274</span>
  <span class="txt brand">Ashgrove<br>Realty<br>Group</span>
  <span class="txt web">www.vantorile.com</span>
</section>

</body>
</html>
```